Design and Renovation Company Luxury Business Card

I want to create a luxury business card for a Design and Renovation Firm . We will use our current logo. The company name is 742KAVO. We do not want anything standard. We need a very unique concept.
Please see uploaded inspiration. I really like the textured paper option. I would like the card to be thick with debossing, and/or embossing options. The logo has orange in it but I would like to see the card with and without the orange. I think the orange may make the company feel less high-end. The goal is to elevate the logo not match its vibe per se of the logo. We want something very unique, not standard at all!
I would like a space for :
Logo,
Name,
Position,
Email,
Office number,
Website Address,
Business Address,
Thank you!
Have fun!
Target Market(s)
Home owners Age 35 +
Industry/Entity Type
Design and Renovation
Contact Information for Business Card
Logo, Name, Position, Email, Office number, Website Address, Business Address,.
Colors
Designer to choose colors to be used in the design.
Requirements
Must have
- A luxury designer feel. Must be black or dark grey but open to other luxury ideas.
Nice to have
- Gold, silver, black embossing or debossing. Textured paper design.
Should not have
- A cheap look and feel.

```html
<!DOCTYPE html>
<html lang="en">
<head>
<meta charset="utf-8">
<title>742KAVO Business Card</title>
<link rel="stylesheet" href="https://fonts.googleapis.com/css2?family=Arimo:wght@400;700&display=swap">
<style>
  :root {
    --backdrop: #d6d6d6;
    --card-front: #2e2e2e;
    --card-back: #262626;
    --text-light: #f2f2f2;
    --accent: #f08a1c;
    --rule: #9a9a9a;
    --motif-warm: #3f342a;
    --motif-grey: #474747;
    --pattern-dark: #1b1b1b;
  }
  html, body {
    margin: 0;
    padding: 0;
    width: 1200px;
    height: 800px;
    overflow: hidden;
    background: var(--backdrop);
    font-family: "Arimo", Arial, sans-serif;
  }
  .canvas {
    position: relative;
    width: 1200px;
    height: 800px;
  }
  .card {
    position: absolute;
    top: 240px;
    width: 560px;
    height: 320px;
    border-radius: 16px;
    overflow: hidden;
    box-shadow: 0 10px 24px rgba(0,0,0,0.25);
  }
  .card-front { left: 30px; background: var(--card-front); }
  .card-back  { left: 610px; background: var(--card-back); }

  /* front */
  .company-name {
    position: absolute;
    top: 44px;
    left: 280px;
    margin: 0;
    color: var(--text-light);
    font-size: 36px;
    font-weight: 700;
    line-height: 1;
  }
  .motif-area {
    position: absolute;
    left: 110px;
    top: 112px;
    width: 230px;
    height: 150px;
    background: linear-gradient(135deg, var(--motif-warm) 0%, var(--motif-warm) 45%, var(--motif-grey) 100%);
    opacity: 0.85;
  }
  .accent-tab {
    position: absolute;
    left: 0;
    top: 246px;
    width: 12px;
    height: 40px;
    background: var(--accent);
  }
  .divider {
    position: absolute;
    left: 70px;
    right: 30px;
    top: 222px;
    height: 1px;
    background: var(--rule);
  }
  .person {
    position: absolute;
    left: 70px;
    top: 172px;
  }
  .person-name {
    margin: 0;
    color: var(--accent);
    font-size: 21px;
    font-weight: 700;
    line-height: 1.1;
  }
  .person-role {
    margin: 2px 0 0;
    color: var(--text-light);
    font-size: 14px;
  }
  .contact-list {
    position: absolute;
    left: 70px;
    top: 234px;
    margin: 0;
    padding: 0;
    list-style: none;
    color: var(--text-light);
    font-size: 14px;
  }
  .contact-list li {
    display: flex;
    align-items: center;
    gap: 8px;
    margin-bottom: 5px;
  }
  .contact-icon { width: 11px; height: 11px; flex: none; }
  .email {
    position: absolute;
    right: 30px;
    top: 198px;
    margin: 0;
    color: var(--text-light);
    font-size: 14px;
  }
  .address {
    position: absolute;
    right: 30px;
    top: 232px;
    margin: 0;
    color: var(--text-light);
    font-size: 14px;
    font-style: normal;
    text-align: right;
    line-height: 1.35;
  }

  /* back */
  .pattern-area {
    position: absolute;
    inset: 0;
    background: radial-gradient(ellipse at 40% 50%, #2b2b2b 0%, var(--pattern-dark) 100%);
  }
  .back-name {
    position: absolute;
    right: 40px;
    top: 142px;
    margin: 0;
    color: var(--text-light);
    font-size: 26px;
    font-weight: 700;
    line-height: 1;
  }
</style>
</head>
<body>
<main class="canvas">

  <section class="card card-front" aria-label="Card front">
    <div class="motif-area" role="img" aria-label="Faint enlarged squares motif in warm brown and grey"></div>

    <h1 class="company-name">742KAVO</h1>

    <div class="accent-tab"></div>

    <div class="person">
      <p class="person-name">Marcus Hale</p>
      <p class="person-role">President</p>
    </div>

    <div class="divider"></div>

    <ul class="contact-list">
      <li>
        <svg class="contact-icon" viewBox="0 0 12 12" aria-hidden="true">
          <path d="M2.5 1 L4.5 1 L5.2 3.6 L3.9 4.5 C4.6 6 6 7.4 7.5 8.1 L8.4 6.8 L11 7.5 L11 9.5 C11 10.3 10.3 11 9.5 11 C5 11 1 7 1 2.5 C1 1.7 1.7 1 2.5 1 Z" fill="var(--accent)"/>
        </svg>
        <span>(555) 0142-7789</span>
      </li>
      <li>
        <svg class="contact-icon" viewBox="0 0 12 12" aria-hidden="true">
          <circle cx="6" cy="6" r="5.5" fill="var(--accent)"/>
          <path d="M0.8 6 H11.2 M6 0.5 C3.5 3 3.5 9 6 11.5 M6 0.5 C8.5 3 8.5 9 6 11.5" stroke="var(--card-front)" stroke-width="0.9" fill="none"/>
        </svg>
        <span>www.742KAVO.com</span>
      </li>
    </ul>

    <p class="email">name@742KAVO.com</p>
    <address class="address">2167 Larchmont Avenue<br>Cedar Hollow, NY 10990</address>
  </section>

  <section class="card card-back" aria-label="Card back">
    <div class="pattern-area" role="img" aria-label="Debossed repeating pattern in dark charcoal"></div>
    <p class="back-name">742KAVO</p>
  </section>

</main>
</body>
</html>
```